Luxury Skincare Product Box Packaging Design

Vorastelle is a range of skincare products that help protect, nourish, and strengthen even the most sensitive skin, ensuring it is healthy, glowing, calm, and soft. Skincare practices support skin to enhance its appearance and relieve skin conditions. Your skin reflects your health. It is your body canvas and is an asset. The products contain naturally derived ingredients, aromatherapy oils, sustainable and ethical ingredients, organic ingredients where possible, natural preservatives and Australian oils, fruits, and extracts.

Vorastelle
Tagline is "Where Calm Finds Bloom"

Our products do not contain sulphates, parabens, phthalates, petrochemicals, synthetic colours, nor synthetic fragrances.

Everything about the Vorastelle Skincare name is creative and communicates luxury. Vorastelle from your first glance of the name, you will know that this is a company with excellent products.

By keeping it simple, unique, and elegant is often associated with high quality and is a way to establish trust. Vorastelle is a product that is “pure” and natural, so Vorastelle packaging would look simple, elegant, and clean.

I have uploaded the actual logo design and individual labels for the current skincare range I currently with the ingredients included so you can get an understanding of what I like. I have also added samples of package designs I quite like to assist with your designs.

Each Product box packaging sizes are as follows:

Product One - Exfoliating Herbs: 110mm (H) x 33mm Diameter
Product Two - Probiotic Lotion: 138mm (H) x 33mm Diameter
Product Three - Vitamin A Serum: 120mm (H) x 30mm Diameter
Updates

The Measurements are as follows: Product One: 110mm (H) x 33mm Diameter Product Two: 138mm (H) x 33mm Diameter Product Three: 120mm (H) x 30mm Diameter

Target Market(s)

Women

Requirements
Must have
• Logo, Product Name and ingredients and if you can barcode on the packaging that is the box design I am after
Nice to have
• samples of designs I like but open to suggestions

```html
<!DOCTYPE html>
<html lang="en">
<head>
<meta charset="utf-8">
<title>Vorastelle Vitamin A Serum – Box Dieline</title>
<link href="https://fonts.googleapis.com/css2?family=Montserrat:wght@300;400;600;700&display=swap" rel="stylesheet">
<style>
  :root{
    --paper:#ffffff;
    --cream:#fdfbec;
    --gold-light:#efe5b6;
    --gold:#e3d393;
    --gold-deep:#d6bf72;
    --cut:#f0675f;
    --ink:#1c1c1c;
    --tag-grey:#6d6b66;
    --rose:#b27a68;
    --rose-light:#e0a597;
  }
  *{margin:0;padding:0;box-sizing:border-box}
  html,body{width:1200px;height:1200px;overflow:hidden;background:var(--paper)}
  body{font-family:"Montserrat",sans-serif;color:var(--ink)}
  .dieline{position:relative;width:1200px;height:1200px}
  .dieline-art{position:absolute;left:0;top:0;width:1200px;height:1200px}
  .cut{fill:none;stroke:var(--cut);stroke-width:1.4}

  .back-panel{position:absolute;left:285px;top:301px;width:148px;text-align:center;font-size:9.3px;line-height:12.4px}
  .back-panel p{margin-bottom:12.4px}
  .back-panel strong{font-weight:600}
  .ingredients{text-transform:uppercase}
  .caution{position:absolute;left:289px;top:760px;width:140px;height:84px;border:2px solid var(--ink);
    font-size:8.6px;line-height:13px;font-weight:600;text-align:center;display:flex;align-items:center;justify-content:center;padding:0 6px}
  .claims{position:absolute;left:287px;top:856px;width:146px;display:flex;justify-content:space-between}
  .claim{width:28px;text-align:center;font-size:4.2px;line-height:4.8px;font-weight:600;color:#3a3228}
  .claim-mark{display:block;width:18px;height:18px;margin:0 auto 2px;border-radius:50%;background:var(--gold-deep)}
  .site{position:absolute;left:270px;top:897px;width:178px;text-align:center;font-size:9.8px;font-weight:600}

  .tagline{position:absolute;width:120px;text-align:center;font-size:8.7px;letter-spacing:.38em;color:var(--tag-grey)}
  .brand{position:absolute;left:700px;top:487px;transform:translate(-50%,-50%) rotate(-90deg);
    font-size:46px;font-weight:300;letter-spacing:.04em;color:var(--rose);white-space:nowrap}
  .product-name{position:absolute;left:644px;top:667px;font-size:27.5px;line-height:31.5px;font-weight:300;letter-spacing:.02em}
  .skin-badge{position:absolute;left:645px;top:750px;width:114px;height:16px;
    background:linear-gradient(90deg,var(--rose-light),#9c6a55);color:#fff;font-size:12px;line-height:16px;font-weight:300;text-align:center}
  .volume{position:absolute;left:644px;top:898px;font-size:9.4px}
</style>
</head>
<body>
<div class="dieline">
  <svg class="dieline-art" viewBox="0 0 1920 1920" aria-hidden="false">
    <defs>
      <linearGradient id="wash-top" x1="0" y1="0" x2="0" y2="1">
        <stop offset="0" stop-color="#f6efd0"/><stop offset="1" stop-color="#e4d596"/>
      </linearGradient>
      <linearGradient id="wash-side-a" x1="0" y1="0" x2="0.3" y2="1">
        <stop offset="0" stop-color="#e6d79a"/><stop offset=".35" stop-color="#e3d291"/>
        <stop offset=".42" stop-color="#fbf8e6"/><stop offset="1" stop-color="#fdfbec"/>
      </linearGradient>
      <linearGradient id="wash-front" x1="0" y1="0" x2="0.4" y2="1">
        <stop offset="0" stop-color="#fbf7e2"/><stop offset=".45" stop-color="#f2ebc6"/>
        <stop offset=".8" stop-color="#ece0ad"/><stop offset="1" stop-color="#e2d18e"/>
      </linearGradient>
      <linearGradient id="wash-side-b" x1="0" y1="0" x2="0" y2="1">
        <stop offset="0" stop-color="#fdfbec"/><stop offset=".4" stop-color="#f7f1d6"/>
        <stop offset=".6" stop-color="#e6d596"/><stop offset="1" stop-color="#e3d291"/>
      </linearGradient>
      <linearGradient id="wash-back" x1="0" y1="0" x2="0.2" y2="1">
        <stop offset="0" stop-color="#f3ebc8"/><stop offset=".3" stop-color="#fdfbec"/><stop offset="1" stop-color="#fdfbec"/>
      </linearGradient>
      <radialGradient id="floral-wash" cx=".5" cy=".5" r=".5">
        <stop offset="0" stop-color="#fffdf2" stop-opacity=".85"/><stop offset="1" stop-color="#fffdf2" stop-opacity="0"/>
      </radialGradient>
    </defs>

    <!-- glue flap -->
    <path d="M432,448 L363,484 L363,1447 L432,1482 Z" fill="var(--cream)"/>
    <!-- panels -->
    <rect x="432" y="448" width="284" height="1034" fill="url(#wash-back)"/>
    <rect x="716" y="448" width="285" height="1034" fill="url(#wash-side-a)"/>
    <rect x="1001" y="448" width="284" height="1034" fill="url(#wash-front)"/>
    <rect x="1285" y="448" width="284" height="1034" fill="url(#wash-side-b)"/>
    <!-- floral line illustration area -->
    <ellipse cx="1150" cy="950" rx="300" ry="520" fill="url(#floral-wash)" role="img" aria-label="Delicate white floral and leaf line illustration"/>
    <!-- tuck flap top -->
    <path d="M1001,448 L1001,163 C1001,95 1045,60 1075,60 L1210,60 C1245,60 1285,95 1285,163 L1285,448 Z" fill="url(#wash-top)"/>
    <!-- dust flaps top -->
    <path d="M716,448 L716,418 L735,407 L772,317 L945,317 L980,437 L1001,448 Z" fill="url(#wash-top)"/>
    <path d="M1285,448 L1300,437 L1340,317 L1512,317 L1548,407 L1569,418 L1569,448 Z" fill="var(--cream)"/>
    <!-- bottom tuck flap -->
    <path d="M432,1482 L432,1767 C432,1835 475,1870 520,1870 L630,1870 C680,1870 716,1835 716,1767 L716,1482 Z" fill="var(--cream)"/>
    <!-- dust flaps bottom -->
    <path d="M716,1482 L733,1497 L770,1612 L945,1612 L980,1525 L1001,1512 L1001,1482 Z" fill="var(--cream)"/>
    <path d="M1285,1482 L1285,1512 L1305,1525 L1340,1612 L1512,1612 L1555,1497 L1569,1482 Z" fill="var(--gold)"/>

    <!-- cut and fold lines -->
    <g class="cut">
      <path d="M432,448 L363,484 L363,1447 L432,1482"/>
      <rect x="432" y="448" width="1137" height="1034"/>
      <path d="M716,448 V1482 M1001,448 V1482 M1285,448 V1482"/>
      <path d="M1001,448 L1001,163 C1001,95 1045,60 1075,60 L1210,60 C1245,60 1285,95 1285,163 L1285,448 M1001,163 H1285"/>
      <path d="M716,448 L716,418 L735,407 L772,317 L945,317 L980,437 L1001,448"/>
      <path d="M1285,448 L1300,437 L1340,317 L1512,317 L1548,407 L1569,418 L1569,448"/>
      <path d="M432,1482 L432,1767 C432,1835 475,1870 520,1870 L630,1870 C680,1870 716,1835 716,1767 L716,1482 M432,1767 H716"/>
      <path d="M716,1482 L733,1497 L770,1612 L945,1612 L980,1525 L1001,1512"/>
      <path d="M1285,1512 L1305,1525 L1340,1612 L1512,1612 L1555,1497 L1569,1482"/>
    </g>
  </svg>

  <!-- back panel -->
  <div class="back-panel">
    <p><strong>All Skin Types</strong><br>Particularly beneficial for dry, Mature skins</p>
    <p><strong>Direction:</strong> Massage a small amount into your face at night, avoiding eye area. Follow with your favourite moisturiser. Please note: Do not use on pregnant or breastfeeding women.</p>
    <p class="ingredients"><strong>Ingredients:</strong><br>Simmondsia chinensis (jojoba) seed oil*, persea gratissima (avocado) oil, rosa eglanteria (rosehip) oil*, olea europaea (olive) fruit oil*, hippophae rhamnoides (seabuck-thorn berry) kernal extract*, tocopherol (vitamin E), retinyl palmitate (vitamin A), glycine soja oilboswel-lia carterii oil (frankincense), pelargonium roseum leaf oil, (rose geranium), cananga odorata flower oil (ylang ylang), rosmarinus officianlis leaf extract<br><strong>*Organic ingredients</strong></p>
  </div>
  <div class="caution">Store in a cool dry place Caution For external use only. Avoid contact with eyes. If irritation occurs, discontinue use.</div>
  <div class="claims">
    <div class="claim"><span class="claim-mark" role="img" aria-label="Australian made icon"></span>Australian Made</div>
    <div class="claim"><span class="claim-mark" role="img" aria-label="Vegan icon"></span>100% Vegan</div>
    <div class="claim"><span class="claim-mark" role="img" aria-label="Cruelty free icon"></span>Cruelty Free</div>
    <div class="claim"><span class="claim-mark" role="img" aria-label="Recycle icon"></span>Please Recycle</div>
    <div class="claim"><span class="claim-mark" role="img" aria-label="Six months after opening icon"></span>6 months once open</div>
  </div>
  <div class="site">www.vorastelle.com</div>

  <!-- side panels tagline -->
  <div class="tagline" style="left:476px;top:427px">Where</div>
  <div class="tagline" style="left:476px;top:541px">Calm</div>
  <div class="tagline" style="left:476px;top:655px">Finds</div>
  <div class="tagline" style="left:476px;top:769px">Bloom</div>
  <div class="tagline" style="left:831px;top:427px">Where</div>
  <div class="tagline" style="left:831px;top:541px">Calm</div>
  <div class="tagline" style="left:831px;top:655px">Finds</div>
  <div class="tagline" style="left:831px;top:769px">Bloom</div>

  <!-- front panel -->
  <div class="brand">Vorastelle</div>
  <h1 class="product-name" style="font-weight:300">VITAMIN A<br>SERUM</h1>
  <div class="skin-badge">ALL SKIN TYPES</div>
  <div class="volume">30 ml</div>
</div>
</body>
</html>
```